Clean, minimal label design needed for new skincare line.

Want clean, minimal labels for Clean (non-toxic), cosmeceutical grade Australian-made skincare products. We are going for a minimal and simple approach to our branding so want the labelling to follow suit. Please find logos attached below. Labels are white and logo is black. Font to be black, avoid colours other than white or black.

Target Market(s)

25-65+

Industry/Entity Type

Beauty

Requirements
Must have
• On the front:
- logo
- product name eg. moisturiser 1
- descriptive words eg. light
- weight eg. 30mls/1 fl oz

On the back:
- directions eg. apply one pump both AM and PM after serum application and prior to barrier protect application.
- Cruelty free icon
- Vegan icon
- Made in Australia Icon
- Open jar with 12M Icon
Nice to have
• See above
Should not have
• Avoid colours other than white or black.

```html
<!DOCTYPE html>
<html lang="en">
<head>
<meta charset="utf-8">
<title>stillwellco. skincare – moisturiser 1 labels</title>
<link rel="stylesheet" href="https://fonts.googleapis.com/css2?family=Montserrat:wght@400;600;700;800&display=swap">
<style>
  :root {
    --ink: #111111;
    --paper: #ffffff;
    --backdrop: #efefef;
    --edge: #dcdcdc;
  }
  * { margin: 0; padding: 0; box-sizing: border-box; }
  html, body {
    width: 1200px;
    height: 1200px;
    overflow: hidden;
    background: var(--backdrop);
    font-family: "Montserrat", sans-serif;
    color: var(--ink);
  }
  .canvas {
    position: relative;
    width: 1200px;
    height: 1200px;
  }
  .label {
    position: absolute;
    top: 320px;
    width: 420px;
    height: 560px;
    background: var(--paper);
    border: 1px solid var(--edge);
    display: flex;
    flex-direction: column;
    align-items: center;
    text-align: center;
  }
  .label--front { left: 140px; }
  .label--back { left: 640px; }

  /* front */
  .brand {
    margin-top: 170px;
    font-size: 50px;
    font-weight: 800;
    letter-spacing: -1.5px;
    line-height: 1;
  }
  .brand-sub {
    margin-top: 6px;
    font-size: 20px;
    font-weight: 600;
  }
  .product-name {
    margin-top: 78px;
    font-size: 22px;
    font-weight: 700;
  }
  .product-descriptor {
    margin-top: 10px;
    width: 120px;
    border: 2px solid var(--ink);
    font-size: 21px;
    font-weight: 400;
    letter-spacing: 1px;
    line-height: 1.2;
    padding: 1px 0;
  }
  .product-volume {
    margin-top: 46px;
    font-size: 15px;
    font-weight: 600;
  }

  /* back */
  .directions-title {
    margin-top: 70px;
    font-size: 17px;
    font-weight: 700;
  }
  .directions-text {
    margin-top: 24px;
    width: 270px;
    font-size: 19px;
    font-weight: 400;
    line-height: 1.3;
  }
  .caution {
    margin-top: 82px;
    font-size: 11px;
    font-weight: 400;
  }
  .badges {
    margin-top: 34px;
    display: flex;
    gap: 22px;
    align-items: center;
  }
  .badge { width: 34px; height: 34px; display: block; }
</style>
</head>
<body>
<main class="canvas">

  <section class="label label--front" aria-label="Front label">
    <h1 class="brand">stillwellco.</h1>
    <p class="brand-sub">skincare</p>
    <h2 class="product-name">moisturiser 1</h2>
    <p class="product-descriptor">light</p>
    <p class="product-volume">30 mls/1 fl oz</p>
  </section>

  <section class="label label--back" aria-label="Back label">
    <h2 class="directions-title">Directions:</h2>
    <p class="directions-text">apply one pump both AM and PM after serum application and prior to barrier protect application.</p>
    <p class="caution">Caution : for external use only use only as directed.</p>
    <div class="badges">
      <svg class="badge" viewBox="0 0 34 34" role="img" aria-label="Vegan badge">
        <circle cx="17" cy="17" r="15" fill="none" stroke="var(--ink)" stroke-width="2.5"/>
      </svg>
      <svg class="badge" viewBox="0 0 34 34" role="img" aria-label="Cruelty free badge">
        <rect x="4" y="4" width="26" height="26" fill="none" stroke="var(--ink)" stroke-width="2.5"/>
      </svg>
      <svg class="badge" viewBox="0 0 34 34" role="img" aria-label="Australian made badge">
        <rect x="4" y="4" width="26" height="26" fill="var(--ink)"/>
      </svg>
      <svg class="badge" viewBox="0 0 34 34" role="img" aria-label="Use within 12 months of opening">
        <path d="M5 8 L27 3" stroke="var(--ink)" stroke-width="2" fill="none"/>
        <rect x="5" y="12" width="24" height="18" rx="2" fill="none" stroke="var(--ink)" stroke-width="2"/>
        <text x="17" y="25" text-anchor="middle" font-family="Montserrat, sans-serif" font-size="8" font-weight="700" fill="var(--ink)">12M</text>
      </svg>
    </div>
  </section>

</main>
</body>
</html>
```